Corbin Lantern Lighting - Commercial & Residential Landscape Lighting

Landscape Lighting Services & Design: Create a website for our landscape lighting company. We would like the design to be tailored around this description:
Illuminate with Confidence. Designed with Precision. Installed with Care.
Locally and veteran-owned, we take pride in transforming outdoor spaces through innovative lighting solutions tailored to your vision. From landscape and holiday lighting to permanent installations, our effortless process and expert design deliver breathtaking results and lasting curb appeal. Backed by a lifetime warranty and quarterly service options, our commitment to quality and customer satisfaction is unwavering. Try before you buy and experience your home in a whole new light with our complimentary demo kit — see the stunning effects before you decide.
- Also, add in this information as well; Outdoor Lighting not only beautifies spaces but also significantly enhances safety by illuminating your home or business. Beautifully lit entrances deter potential intruders, making your home a safer place for your loved ones. we also offer quarterly service plans to ensure lighting equipment continues to operate & illuminate effectively throughout the year. Also mention we provide free estimates and we are offering a 10% discount to military, veterans, and first responders.

Target Market(s)

Luxury market

Industry/Entity Type

Landscape Lighting - Residential & Commercial Lighting Services

Coding

Coded - Design and coding required

Number of Pages Required

2 page

Colors
00AB8E
00BBA5
67D7C9
C6EFE9
E9F9F6
59FF00
82FF00
B8FF75
E3FFCB
F4FFEA
FFC000
F8CF3A
FAE287
FDF2CF
FEFAEE

Requirements
Must have
• a lead generation button where people can submit their information for us to reach out to them and schedule their free estimate, homepage, about page, contact page, products and services page, user friendly, easy to navigate, and it also must be engaging and eye popping, as well as appealing to the luxury market. Please use colors; verdent green, dark green, ivory, and sunny yellow. Also, include an about page that references our story; Derek is retired Army and he opened a fitness studio in 2017 with his wife Vanessa. He has installed low voltage lighting in every home he lived in and for his friends and family over the years and decided to open his own business because he is passionate about beautifying outdoor landscapes and highlighting a properties full potential, not only in the day but at night as well all while providing safety and security for his clients. Having a deep respect for nature and landscaping, he wants to provide the same care and quality to each of his clients as he has in the fitness industry for decades. He believes small businesses are the back bone of America and he's excited to provide a service that is all to often neglected in the design of a home.
Nice to have
• I would like to have a clear intent and purpose, engaging web design, clear call to action, optimized for search engines, mobile friendy design, security measures, credibility indicators

```html
<!DOCTYPE html>
<html lang="en">
<head>
<meta charset="utf-8">
<title>Corbin Lantern Lighting – Residential &amp; Commercial Landscape Lighting</title>
<link href="https://fonts.googleapis.com/css2?family=Lato:wght@400;700;900&family=Poppins:wght@400;500&display=swap" rel="stylesheet">
<style>
:root{
  --green:#1a9f80;
  --green-dark:#12806a;
  --teal-band:#2aa98d;
  --mint:#e4fbf7;
  --yellow:#fbb829;
  --yellow-soft:#f8cf3a;
  --ink:#1d1d1d;
  --text:#3d3d3d;
  --footer:#0b0b0b;
  --white:#ffffff;
}
*{margin:0;padding:0;box-sizing:border-box}
html,body{width:1200px;height:4160px;overflow:hidden}
body{position:relative;font-family:"Lato",sans-serif;color:var(--text);background:var(--white)}
.abs{position:absolute}
a{color:inherit;text-decoration:none}
.btn{position:absolute;display:flex;align-items:center;justify-content:center;background:var(--yellow);color:#1b1b1b;font-weight:700;font-size:17px;border-radius:6px}

/* top bar & header */
.topbar{left:396px;top:0;width:804px;height:32px;background:var(--yellow);clip-path:polygon(32px 0,100% 0,100% 100%,0 100%);display:flex;align-items:center;font-size:14px;color:#222}
.topbar .item{display:flex;align-items:center;gap:8px;margin-left:72px}
.topbar .item:first-child{margin-left:74px}
.topbar .socials{display:flex;gap:12px;margin-left:84px}
.dot-icon{width:20px;height:20px;border-radius:50%;background:var(--green)}
.ico{width:20px;height:20px;border-radius:50%;background:var(--green);display:flex;align-items:center;justify-content:center}
.brand{left:110px;top:18px;width:190px}
.brand .name{font-size:34px;font-weight:700;color:#c4262e;letter-spacing:1px;line-height:1}
.brand .tag{font-size:10px;color:#3a2f7a;letter-spacing:1.3px;margin-top:6px;font-weight:700}
.nav{left:509px;top:58px;display:flex;gap:30px;font-size:15px;color:#222}
.nav .active{color:var(--green);text-decoration:underline;text-underline-offset:4px}
.header-cta{left:945px;top:46px;width:145px;height:47px;font-size:16px}

/* hero */
.hero-photo{left:0;top:102px;width:1200px;height:498px;background:linear-gradient(180deg,#3e5b74 0%,#5f6c62 40%,#3f5c2c 75%,#51752f 100%)}
.hero-title{left:107px;top:183px;font-size:52px;line-height:64px;font-weight:900;color:#fff;text-shadow:0 2px 8px rgba(0,0,0,.35)}
.hero-edge{left:0;top:500px;width:1200px;height:110px}

/* section labels */
.label{display:flex;align-items:center;gap:14px;font-size:16px;font-weight:700;color:#1d1d1d}
.bars{display:flex;flex-direction:column;gap:4px}
.bars i{display:block;width:12px;height:2px;background:var(--yellow)}
.h2{font-size:39px;font-weight:700;color:var(--green);line-height:52px}
.h2 em{font-style:normal;color:var(--yellow)}

/* welcome */
.welcome-list{left:643px;top:792px;width:440px;font-size:14px;line-height:26px;color:#333}
.welcome-list li{list-style:none;position:relative;padding-left:27px;margin-bottom:8px}
.welcome-list svg{position:absolute;left:0;top:8px}

/* about */
.about-bg{left:0;top:1232px;width:1200px;height:614px;background:var(--mint)}
.about-copy{left:110px;top:1466px;width:448px;font-size:14px;line-height:26px;color:#333}

/* bands */
.band{left:0;width:1200px;background:linear-gradient(135deg,#2ea78c,#1f9c80 55%,#2caa90);color:#fff;text-align:center}
.band h3{font-size:38px;font-weight:700}
.band p{font-size:14px}

/* services */
.card{width:305px;height:303px;border-radius:4px;overflow:hidden}
.card .photo{position:absolute;left:0;top:0;width:100%;height:100%}
.card .cap{position:absolute;left:0;bottom:0;width:100%;background:var(--green);color:#fff;clip-path:polygon(0 22px,20% 8px,50% 0,80% 8px,100% 22px,100% 100%,0 100%)}
.card .cap h4{font-size:25px;font-weight:700;text-align:center}
.arrow{width:28px;height:28px;border-radius:50%;border:1.5px solid var(--green);display:flex;align-items:center;justify-content:center}

/* form */
.field{left:643px;width:445px;height:44px;background:#fff;border-radius:5px;box-shadow:0 2px 8px rgba(0,0,0,.13);display:flex;align-items:center;padding-left:22px;gap:12px;font-size:14px;color:#777}

/* footer */
.footer{left:0;top:3811px;width:1200px;height:349px;background:var(--footer);color:#fff}
.footer h5{font-size:21px;font-weight:700;color:var(--yellow)}
.flinks{list-style:none;font-family:"Poppins",sans-serif;font-size:15px}
.flinks li{display:flex;align-items:center;gap:12px;height:32.5px}
.flinks li::before{content:"";width:8px;height:8px;border-radius:50%;background:var(--yellow)}
.fcontact{font-family:"Poppins",sans-serif;font-size:15px}
.fcontact div{display:flex;align-items:flex-start;gap:10px;margin-bottom:11px}
.yico{width:22px;height:22px;border-radius:50%;background:var(--yellow);flex:none}
</style>
</head>
<body>

<!-- header -->
<div class="abs topbar">
  <div class="item">
    <span class="ico"><svg width="11" height="11" viewBox="0 0 24 24"><path fill="#fff" d="M6.6 10.8a15 15 0 006.6 6.6l2.2-2.2c.3-.3.7-.4 1-.2 1.1.4 2.3.6 3.6.6.6 0 1 .4 1 1V20c0 .6-.4 1-1 1A17 17 0 013 4c0-.6.4-1 1-1h3.5c.6 0 1 .4 1 1 0 1.3.2 2.5.6 3.6.1.3 0 .7-.2 1z"/></svg></span>
    888 888 88
  </div>
  <div class="item">
    <span class="ico"><svg width="11" height="9" viewBox="0 0 24 18"><path fill="#fff" d="M0 0h24v18H0z"/><path d="M0 0l12 9 12-9" stroke="#1a9f80" stroke-width="2" fill="none"/></svg></span>
    info@corbinlanternlighting.com
  </div>
  <div class="socials"><span class="dot-icon"></span><span class="dot-icon"></span><span class="dot-icon"></span><span class="dot-icon"></span></div>
</div>
<div class="abs brand">
  <div class="name">CORBIN</div>
  <div class="tag">LANTERN LIGHTING</div>
</div>
<nav class="abs nav">
  <a class="active">Home</a><a>About</a><a>Services</a><a>Products</a><a>Testimonials</a>
</nav>
<a class="btn header-cta">Contact Us</a>

<!-- hero -->
<div class="abs hero-photo" role="img" aria-label="Brick house at dusk with lit landscape and lawn"></div>
<h1 class="abs hero-title">Illuminate with Confidence.<br>Designed with Precision.<br>Installed with Care.</h1>
<a class="btn" style="left:110px;top:404px;width:273px;height:45px">Schedule Your Free Estimate</a>
<svg class="abs hero-edge" viewBox="0 0 1200 110" preserveAspectRatio="none">
  <path d="M0 28 Q300 55 600 95 Q900 55 1200 28 L1200 110 L0 110Z" fill="var(--green)"/>
  <path d="M0 40 Q300 70 600 100 Q900 70 1200 40 L1200 110 L0 110Z" fill="#fff"/>
</svg>

<!-- welcome -->
<div class="abs label" style="left:548px;top:680px"><span class="bars"><i></i><i></i><i></i></span>Welcome</div>
<h2 class="abs h2" style="left:0;top:708px;width:1200px;text-align:center">Welcome to <em>Corbin Lantern Lighting</em></h2>
<svg class="abs" style="left:108px;top:792px" width="452" height="356" viewBox="0 0 452 356" role="img" aria-label="House with landscape lighting at night">
  <defs><linearGradient id="gw" x1="0" y1="0" x2="0" y2="1"><stop offset="0" stop-color="#2d3d45"/><stop offset=".55" stop-color="#6a4f34"/><stop offset="1" stop-color="#2b3a22"/></linearGradient></defs>
  <path d="M3 70 Q3 60 14 56 L226 3 L438 56 Q449 60 449 70 L449 340 Q449 353 436 353 L16 353 Q3 353 3 340Z" fill="url(#gw)" stroke="var(--green)" stroke-width="4"/>
</svg>
<ul class="abs welcome-list">
  <li><svg width="14" height="10" viewBox="0 0 14 10"><path d="M0 5h12M8 1l4 4-4 4" stroke="var(--green)" stroke-width="1.6" fill="none"/></svg>Locally and veteran-owned, we take pride in transforming outdoor spaces through innovative lighting solutions tailored to your vision. From landscape and holiday lighting to permanent installations, our effortless process and expert design deliver breathtaking results and lasting curb appeal. Backed by a lifetime warranty and quarterly service options, our commitment to quality and customer satisfaction is unwavering.</li>
  <li><svg width="14" height="10" viewBox="0 0 14 10"><path d="M0 5h12M8 1l4 4-4 4" stroke="var(--green)" stroke-width="1.6" fill="none"/></svg>Outdoor Lighting not only beautifies spaces but also significantly enhances safety by illuminating your home or business. Beautifully lit entrances deter potential intruders,</li>
</ul>
<a class="btn" style="left:643px;top:1098px;width:128px;height:45px">Read More</a>

<!-- about -->
<div class="abs about-bg"></div>
<div class="abs label" style="left:110px;top:1322px"><span class="bars"><i></i><i></i><i></i></span>About Us</div>
<h2 class="abs h2" style="left:110px;top:1348px;width:420px">Built with Purpose. <em>Lit with Passion.</em></h2>
<p class="abs about-copy">Derek is retired Army and he opened a fitness studio in 2017 with his wife Vanessa. He has installed low voltage lighting in every home he lived in and for his friends and family over the years and decided to open his own business because he is passionate about beautifying outdoor landscapes and highlighting a properties full potential, not only in the day but at night as well all while providing safety and security for his clients. Having a deep respect for nature and landscaping, he wants to provide the same care and quality to</p>
<a class="btn" style="left:110px;top:1709px;width:128px;height:45px">Read More</a>
<svg class="abs" style="left:663px;top:1314px" width="406" height="444" viewBox="0 0 406 444" role="img" aria-label="Portrait of the company founder">
  <polygon points="203,4 402,115 402,329 203,440 4,329 4,115" fill="#eceef0" stroke="var(--green)" stroke-width="5"/>
</svg>

<!-- demo kit band -->
<section class="abs band" style="top:1846px;height:329px" role="img" aria-label="Lit modern house under teal overlay">
  <h3 style="margin-top:78px">See Your Home in a Whole New Light – On Us</h3>
  <p style="margin-top:14px">Try before you buy and experience your home in a whole new light with our complimentary Demo kit — see the stunning effects before you decide.</p>
</section>
<a class="btn" style="left:500px;top:2043px;width:197px;height:44px">Get My Free Demo Kit</a>

<!-- services -->
<div class="abs label" style="left:534px;top:2260px"><span class="bars"><i></i><i></i><i></i></span>Our Services</div>
<h2 class="abs h2" style="left:250px;top:2288px;width:700px;text-align:center">Innovative Lighting Solutions <em>Tailored to Your Vision</em></h2>
<div class="abs arrow" style="left:46px;top:2551px"><svg width="10" height="10" viewBox="0 0 10 10"><path d="M6 1L2 5l4 4" stroke="var(--green)" stroke-width="1.5" fill="none"/></svg></div>
<div class="abs arrow" style="left:1129px;top:2551px;border-color:#333"><svg width="10" height="10" viewBox="0 0 10 10"><path d="M4 1l4 4-4 4" stroke="#333" stroke-width="1.5" fill="none"/></svg></div>

<div class="abs card" style="left:110px;top:2413px">
  <div class="photo" role="img" aria-label="Lit stone path leading to a front door" style="background:linear-gradient(180deg,#3b3a38,#7a5a35 60%,#584a3b)"></div>
  <div class="cap" style="height:82px;padding-top:30px"><h4>Landscape Lighting</h4></div>
</div>
<div class="abs card" style="left:445px;top:2411px;width:309px;height:307px;border:3px solid var(--green)">
  <div class="photo" role="img" aria-label="Garden path lined with permanent path lights" style="background:linear-gradient(180deg,#243528,#3e5a3a 55%,#5a6a4c)"></div>
  <div class="cap" style="height:148px;background:var(--yellow);padding:36px 16px 0;text-align:left">
    <h4 style="text-align:left;font-size:25px">Permanent Installations</h4>
    <p style="font-size:13px;margin-top:8px">Year-round brilliance with low maintenance</p>
    <p style="font-size:12px;margin-top:10px">Read More...</p>
  </div>
</div>
<div class="abs card" style="left:783px;top:2413px">
  <div class="photo" role="img" aria-label="Illuminated outdoor steps beside a modern home" style="background:linear-gradient(180deg,#3c4550,#666a6c 55%,#8a8a86)"></div>
  <div class="cap" style="height:82px;padding-top:30px"><h4>Safety Lighting</h4></div>
</div>

<!-- serving band -->
<section class="abs band" style="top:2829px;height:374px" role="img" aria-label="House front at dusk under teal overlay">
  <h3 style="margin-top:78px">Proudly Serving Those Who Serve</h3>
  <p style="margin-top:14px">We proudly offer free estimates and a 10% discount for military, veterans, and first responders.</p>
</section>
<div class="abs" style="left:300px;top:3005px;width:110px;height:110px;border-radius:50%;background:var(--yellow-soft);display:flex;align-items:center;justify-content:center;font-size:40px;font-weight:900;color:var(--green-dark)">10%</div>
<a class="btn" style="left:478px;top:3039px;width:239px;height:44px">Schedule My Free Estimate</a>

<!-- contact -->
<div class="abs label" style="left:534px;top:3290px"><span class="bars"><i></i><i></i><i></i></span>Contact Us</div>
<h2 class="abs h2" style="left:0;top:3318px;width:1200px;text-align:center">Let’s Light <em>Up Your Vision</em></h2>
<svg class="abs" style="left:108px;top:3388px" width="452" height="326" viewBox="0 0 452 326" role="img" aria-label="Two-storey modern home lit at night">
  <defs><linearGradient id="gc" x1="0" y1="0" x2="0" y2="1"><stop offset="0" stop-color="#1c3e7a"/><stop offset=".6" stop-color="#8a7350"/><stop offset="1" stop-color="#333a35"/></linearGradient></defs>
  <path d="M3 70 Q3 60 14 56 L226 3 L438 56 Q449 60 449 70 L449 310 Q449 323 436 323 L16 323 Q3 323 3 310Z" fill="url(#gc)" stroke="var(--green)" stroke-width="4"/>
</svg>
<div class="abs field" style="top:3408px"><svg width="15" height="15" viewBox="0 0 16 16"><circle cx="8" cy="5" r="4" fill="#888"/><path d="M0 16a8 6 0 0116 0z" fill="#888"/></svg>Name</div>
<div class="abs field" style="top:3469px"><svg width="16" height="12" viewBox="0 0 16 12"><rect width="16" height="12" fill="#888"/><path d="M0 0l8 6 8-6" stroke="#fff" fill="none"/></svg>Email</div>
<div class="abs field" style="top:3527px"><svg width="15" height="15" viewBox="0 0 16 16"><rect x="1" y="2" width="14" height="13" fill="none" stroke="#888" stroke-width="1.6"/><path d="M1 6h14" stroke="#888" stroke-width="1.6"/></svg>Project Type<svg style="margin-left:auto;margin-right:22px" width="12" height="8" viewBox="0 0 12 8"><path d="M1 1l5 5 5-5" stroke="#555" stroke-width="1.5" fill="none"/></svg></div>
<div class="abs field" style="top:3588px"><svg width="15" height="15" viewBox="0 0 24 24"><path fill="#888" d="M6.6 10.8a15 15 0 006.6 6.6l2.2-2.2c.3-.3.7-.4 1-.2 1.1.4 2.3.6 3.6.6.6 0 1 .4 1 1V20c0 .6-.4 1-1 1A17 17 0 013 4c0-.6.4-1 1-1h3.5c.6 0 1 .4 1 1 0 1.3.2 2.5.6 3.6.1.3 0 .7-.2 1z"/></svg>Phone Number</div>
<a class="btn" style="left:649px;top:3666px;width:196px;height:45px;color:#fff;font-size:16px">Submit</a>

<!-- footer -->
<svg class="abs" style="left:0;top:3790px" width="1200" height="40" viewBox="0 0 1200 40" preserveAspectRatio="none">
  <path d="M0 32 Q600 -6 1200 32 L1200 40 L0 40Z" fill="var(--green)"/>
  <path d="M0 38 Q600 2 1200 38 L1200 40 L0 40Z" fill="var(--footer)"/>
</svg>
<footer class="abs footer">
  <h5 class="abs" style="left:216px;top:90px">Quick Links</h5>
  <ul class="abs flinks" style="left:216px;top:118px">
    <li>Home</li><li>About</li><li>Services</li><li>Products</li><li>Schedule</li>
  </ul>
  <div class="abs" style="left:450px;top:110px;width:300px;text-align:center">
    <div style="font-size:46px;font-weight:700;color:var(--yellow);letter-spacing:2px;line-height:1">CORBIN</div>
    <div style="font-size:14px;color:var(--yellow);letter-spacing:3px;margin-top:6px">LANTERN LIGHTING</div>
  </div>
  <div class="abs" style="left:544px;top:213px;display:flex;gap:14px">
    <span class="yico" style="width:26px;height:26px"></span><span style="width:26px;height:26px;border-radius:50%;background:#fff"></span><span style="width:26px;height:26px;border-radius:50%;background:#fff"></span>
  </div>
  <h5 class="abs" style="left:824px;top:90px">Contact Us</h5>
  <div class="abs fcontact" style="left:826px;top:128px">
    <div><span class="yico"></span>888 888 888</div>
    <div><span class="yico"></span>info@corbinlanternlighting.com</div>
    <div><span class="yico"></span><span>1234 Oakview Lane<br>YourCity, YourState ZIP</span></div>
  </div>
  <div class="abs" style="left:110px;top:296px;width:980px;height:1px;background:#3a3a3a"></div>
  <p class="abs" style="left:0;top:312px;width:1200px;text-align:center;font-size:14px">Copyright © 2025 Corbin Lantern Lighting. All rights reserved.</p>
</footer>

</body>
</html>
```